Catholic composer needs poster for new musical, "THE STONE AND THE VIGIL, the Harvest Musical"

We need a dynamic poster for "The Stone and the Vigil," a new musical written for Catholic dinner theater. We need you to create an iconic design like you see in posters for classic musicals, like "Rosa Calendula," Lantern of the Harbour," or "Gilded." In our musical, “fire” represents the Holy Spirit, who showers man with his merciful love.

Miraculous events occur. A mighty wind from heaven fills the house. Tongues of fire appear over their heads. They speak in other tongues that are understandable by all present. They are emboldened to go out and tell the Good News to the world, despite the risks associated with evangelizing this fledgling religion. They exclaim, “Lord, you will show us the path to life.”

Target Market(s)

The audience is adult members of Catholic churches. But don't make the design look too "churchy."

Requirements
Must have
• Photoshop or Illustrated file with layers, or vector format.
Should not have
• Really don't want photos.

```html
<!DOCTYPE html>
<html lang="en">
<head>
<meta charset="utf-8">
<title>The Stone and the Vigil – The Harvest Musical</title>
<link rel="stylesheet" href="https://fonts.googleapis.com/css2?family=Cormorant+Garamond:wght@600&family=Dancing+Script:wght@500&family=Open+Sans:wght@600;700&display=swap">
<style>
  :root {
    --orange: #f08a24;
    --orange-deep: #e8731a;
    --purple: #6a2c91;
    --flame-gold: #f5a623;
    --flame-yellow: #fbd25a;
    --flame-purple: #8a4cb0;
    --sky: #cfe9f5;
    --white: #ffffff;
  }
  * { margin: 0; padding: 0; box-sizing: border-box; }
  html, body { width: 900px; height: 1200px; overflow: hidden; background: var(--white); }
  .poster {
    position: relative;
    width: 900px;
    height: 1200px;
    overflow: hidden;
    background: linear-gradient(to bottom, var(--white) 0%, var(--white) 55%, var(--sky) 100%);
    font-family: "Open Sans", sans-serif;
  }
  .flame-art {
    position: absolute;
    left: 110px;
    top: 170px;
    width: 640px;
    height: 1000px;
    border-radius: 55% 45% 50% 50% / 70% 70% 30% 30%;
    background:
      radial-gradient(ellipse at 55% 55%, rgba(138,76,176,0.75) 0%, rgba(138,76,176,0) 40%),
      radial-gradient(ellipse at 40% 70%, var(--flame-gold) 0%, rgba(251,210,90,0.85) 45%, rgba(251,210,90,0) 75%);
    opacity: 0.9;
  }
  .invocation {
    position: absolute;
    left: 48px;
    top: 30px;
    font-family: "Dancing Script", cursive;
    font-size: 54px;
    line-height: 1.05;
    color: var(--orange);
  }
  .title {
    position: absolute;
    right: 30px;
    top: 430px;
    width: 460px;
    text-align: right;
    font-family: "Cormorant Garamond", serif;
    font-weight: 600;
    font-size: 84px;
    line-height: 0.98;
    color: var(--purple);
  }
  .title-line { display: block; }
  .subtitle-band {
    position: absolute;
    left: 510px;
    top: 624px;
    width: 390px;
    height: 44px;
    background: linear-gradient(to right, var(--orange-deep), var(--orange) 60%, rgba(240,138,36,0.4));
    color: var(--white);
    font-weight: 700;
    font-size: 26px;
    line-height: 44px;
    padding-left: 26px;
  }
  .tagline {
    position: absolute;
    left: 45px;
    top: 700px;
    color: var(--purple);
    font-weight: 700;
    font-size: 37px;
    line-height: 1.25;
  }
  .event-details {
    position: absolute;
    left: 588px;
    top: 955px;
    color: var(--purple);
    font-weight: 700;
    font-size: 29px;
    line-height: 1.3;
    list-style: none;
  }
  .website {
    position: absolute;
    left: 0;
    width: 900px;
    top: 1128px;
    text-align: center;
    color: var(--orange);
    font-size: 30px;
    font-weight: 600;
  }
</style>
</head>
<body>
  <main class="poster">
    <div class="flame-art" role="img" aria-label="Stylised tongues of fire in yellow, orange and purple rising upward"></div>

    <p class="invocation">“O Spirit come,<br>You are merciful love”</p>

    <h1 class="title">
      <span class="title-line">The Stone</span>
      <span class="title-line">and the Vigil</span>
    </h1>

    <div class="subtitle-band">The Harvest Musical</div>

    <p class="tagline">A new musical for Catholic Dinner Theater<br>By Daniel Ashcombe</p>

    <ul class="event-details">
      <li>Where: Lorem Dium</li>
      <li>Date: Sep, 23, 2015</li>
      <li>Time: 7:00 PM</li>
      <li>Ticket Prices: $25.00</li>
    </ul>

    <p class="website">www.TheStoneAndTheVigil.com</p>
  </main>
</body>
</html>
```